Biz Card Design TPWA

New business card for a new company.
Logo was completed by a designer on ArtHivePro and looking to continue requesting additional services.
Company Name: Tidal Peak Watt Advisors
Although this company is starting in Canada, we will be moving towards a global presence within the next 6 months.
Key elements to this business are as follows.
Energy Procurement
Energy Reduction Services
Demand Side Consulting
Energy Efficiency Consulting
Saving Clients Money
Helping Them Go "Green"
Managing Their Energy Requirements
Basically the goal for our company is to find the best procurement solution for our clients and reduce their energy consumption. This reduces their expenses and the amount of greenhouse gas they produce on a daily basis.
I have been in the energy footprint for the last 20 years and know that most companies are looking to "do whatever is necessary to get them to sign on the dotted line". I would prefer to walk away from a client that I can't help than to put them into a situation that they will regret for years to come. This is where the "TIDAL" part of the company name comes from.
The following is a catch phrase that encompasses what we do.
"Reducing your carbon footprint & energy bill at the same time!"
The back of the card needs to have this statement along with some sort of illustration. The back is a playground for creative ideas.
The front of the card needs the following.
Logo.
First & Last Name (Gus Marwick)
Title (Energy Warrior)
Phone Number (555) 314-2718
Fax Number (555) 271-8314
Email Address gus@tidalpeakwattadvisors-demo.com
Address 47 birchfield ave Toronto Ontario K2K 2K2
I want it to be a card that is remembered when any of my staff give it to a customer. It HAS to stand out.
Target Market(s)
Business Owners, Decision Makers, 30 to 65+
Industry/Entity Type
Business
Look and feel

```html
<!DOCTYPE html>
<html lang="en">
<head>
<meta charset="utf-8">
<title>Tidal Peak Watt Advisors – Business Cards</title>
<link href="https://fonts.googleapis.com/css2?family=Arimo:wght@400;700&display=swap" rel="stylesheet">
<style>
  :root {
    --page-bg: #ecebe8;
    --card-white: #ffffff;
    --green-dark: #0f8f45;
    --green-mid: #3fa85a;
    --green-light: #a9d59a;
    --rule-blue: #2f5fae;
    --heading-blue: #2c5fb0;
    --text-grey: #3a3a3a;
    --name-dark: #0d3d1f;
  }
  * { margin: 0; padding: 0; box-sizing: border-box; }
  html, body { width: 1200px; height: 900px; overflow: hidden; }
  body {
    background: var(--page-bg);
    font-family: "Arimo", Arial, sans-serif;
    display: flex;
    flex-direction: column;
    align-items: center;
    justify-content: center;
    gap: 36px;
  }
  .card {
    position: relative;
    width: 700px;
    height: 400px;
    background: var(--card-white);
    box-shadow: 0 6px 18px rgba(0,0,0,0.12);
    overflow: hidden;
  }

  /* ---------- Back card ---------- */
  .back .band {
    position: absolute;
    left: 0; right: 0;
    top: 40px;
    height: 92px;
    background: linear-gradient(90deg, var(--green-light) 0%, var(--green-mid) 45%, var(--green-dark) 100%);
    border-bottom: 3px solid var(--rule-blue);
  }
  .back .company-name {
    position: absolute;
    right: 34px;
    top: 30px;
    color: var(--card-white);
    font-weight: 700;
    font-size: 30px;
    letter-spacing: -0.3px;
  }
  .back .services {
    position: absolute;
    left: 60px;
    top: 168px;
    right: 40px;
  }
  .back .services-heading {
    color: var(--heading-blue);
    font-weight: 700;
    font-size: 22px;
    margin-bottom: 14px;
  }
  .back .service-columns {
    display: flex;
    gap: 60px;
  }
  .back .service-list {
    list-style: none;
    color: var(--text-grey);
    font-size: 17px;
    line-height: 1.45;
  }
  .back .service-list li::before {
    content: "";
    display: inline-block;
    width: 6px; height: 6px;
    background: var(--green-mid);
    border-radius: 50%;
    margin: 0 12px 3px 0;
    vertical-align: middle;
  }

  /* ---------- Front card ---------- */
  .front .band {
    position: absolute;
    left: 0; right: 0;
    top: 70px;
    height: 104px;
    background: linear-gradient(90deg, var(--green-dark) 0%, var(--green-mid) 55%, var(--green-light) 100%);
    border-top: 3px solid var(--rule-blue);
  }
  .front .person {
    position: absolute;
    left: 40px;
    top: 22px;
  }
  .front .person-name {
    color: var(--name-dark);
    font-size: 30px;
  }
  .front .person-title {
    color: var(--card-white);
    font-size: 20px;
    margin-top: 4px;
  }
  .front .brand-name {
    position: absolute;
    left: 40px;
    bottom: 46px;
    color: var(--heading-blue);
    font-weight: 700;
    font-size: 24px;
    letter-spacing: -0.3px;
  }
  .front .contact-list {
    position: absolute;
    right: 36px;
    top: 206px;
    list-style: none;
    color: var(--text-grey);
    font-size: 16px;
  }
  .front .contact-list li {
    display: flex;
    align-items: center;
    gap: 10px;
    height: 32px;
  }
  .front .icon {
    width: 20px; height: 20px;
    background: var(--green-mid);
    border-radius: 3px;
    display: inline-flex;
    align-items: center;
    justify-content: center;
    flex-shrink: 0;
  }
  .front .icon svg { width: 14px; height: 14px; }
</style>
</head>
<body>

  <section class="card back" aria-label="Business card back">
    <div class="band">
      <span class="company-name">TidalPeakWattAdvisors</span>
    </div>
    <div class="services">
      <h2 class="services-heading">Key elements to this business :</h2>
      <div class="service-columns">
        <ul class="service-list">
          <li>Energy Procurement</li>
          <li>Energy Reduction Services</li>
          <li>Demand Side Consulting</li>
          <li>Energy Efficiency Consulting</li>
        </ul>
        <ul class="service-list">
          <li>Saving Clients Money</li>
          <li>Helping Them Go "Green"</li>
          <li>Managing Their Energy Requirements</li>
        </ul>
      </div>
    </div>
  </section>

  <section class="card front" aria-label="Business card front">
    <div class="band">
      <div class="person">
        <div class="person-name">Gus Marwick</div>
        <div class="person-title">Energy Warrior</div>
      </div>
    </div>

    <ul class="contact-list">
      <li>
        <span class="icon"><svg viewBox="0 0 14 14"><path d="M7 2 L13 7 H11 V12 H3 V7 H1 Z" fill="#fff"/></svg></span>
        47 birchfield ave Toronto Ontario K2K 2K2
      </li>
      <li>
        <span class="icon"><svg viewBox="0 0 14 14"><path d="M3 1.5 L5.5 1.5 L6.5 4.5 L5 5.8 Q6.5 8.5 8.2 9 L9.5 7.5 L12.5 8.5 L12.5 11 Q12.5 12.5 11 12.5 Q3 12 1.5 3 Q1.5 1.5 3 1.5 Z" fill="#fff"/></svg></span>
        (555) 314-2718
        <span class="icon"><svg viewBox="0 0 14 14"><rect x="3" y="1.5" width="8" height="4" fill="#fff"/><rect x="1.5" y="6" width="11" height="5" rx="1" fill="#fff"/><rect x="3.5" y="9" width="7" height="3.5" fill="#fff" stroke="#3fa85a" stroke-width="0.8"/></svg></span>
        (555) 271-8314
      </li>
      <li>
        <span class="icon"><svg viewBox="0 0 14 14"><circle cx="7" cy="7" r="2.3" fill="none" stroke="#fff" stroke-width="1.5"/><path d="M9.3 5 V8 Q9.3 9.8 11 9.5 Q12.5 9 12.5 7 A5.5 5.5 0 1 0 9.5 11.8" fill="none" stroke="#fff" stroke-width="1.5"/></svg></span>
        gus@tidalpeakwattadvisors-demo.com
      </li>
      <li>
        <span class="icon"><svg viewBox="0 0 14 14"><g fill="none" stroke="#fff" stroke-width="1.2"><circle cx="7" cy="7" r="5.5"/><ellipse cx="7" cy="7" rx="2.3" ry="5.5"/><path d="M1.5 7 H12.5 M2.5 4 H11.5 M2.5 10 H11.5"/></g></svg></span>
        www.tidalpeakwattadvisors-demo.com
      </li>
    </ul>

    <div class="brand-name">TidalPeakWattAdvisors</div>
  </section>

</body>
</html>
```